CORAL DRIFT INN GRAND OPENING

We are the new owners and just finished completely remodeling our property and rooms in January 2017. To attract new customers we are planning a HOTEL GRAND OPENING PARTY on FEBRUARY 16 , 2017. EVENT WILL START WITH A 5:00PM HAPPY HOUR
WE WILL HAVE: LIVE MUSIC, SNACKS & BOOZE
The event will be a LUAU PARTY THEME

Industry/Entity Type

Property

Font styles to use
Sans Serif

Colors
85cae6
3176b5
ee3036
cadf82
fbed22
fece3e

Requirements
Must have
• property address:
• 4927 Marlowe Lane
• Harlow Key, Fl 32814
• COMPANY LOGO

```html
<!DOCTYPE html>
<html lang="en">
<head>
<meta charset="UTF-8">
<title>Coral Drift Inn Grand Opening</title>
<link href="https://fonts.googleapis.com/css2?family=Anton&family=Kaushan+Script&family=Montserrat:wght@500;700;800&display=swap" rel="stylesheet">
<style>
  :root {
    --sky: #85cae6;
    --sea: #4fb0cf;
    --deep: #3176b5;
    --band: #2f8fd0;
    --ink: #24363c;
    --white: #ffffff;
    --leaf: #2f8a4c;
    --leaf-dark: #1f6a3a;
    --petal: #e7a6d2;
    --sun: #fece3e;
    --red: #ee3036;
  }
  html, body {
    margin: 0;
    padding: 0;
    overflow: hidden;
    background: #e9f6fb;
  }
  .poster {
    position: relative;
    width: 928px;
    height: 1200px;
    overflow: hidden;
    background: linear-gradient(180deg, #8fd0e8 0%, var(--sea) 55%, #45a9cb 100%);
    font-family: "Montserrat", sans-serif;
    color: var(--white);
  }
  .rays {
    position: absolute;
    inset: 0;
  }
  .wreath {
    position: absolute;
    left: 94px;
    top: 52px;
    width: 740px;
    height: 720px;
  }
  .badge {
    position: absolute;
    left: 220px;
    top: 188px;
    width: 488px;
    height: 488px;
    border-radius: 50%;
    background: var(--ink);
    box-shadow: 0 0 0 10px rgba(255,255,255,0.0), 0 0 0 12px var(--white);
    text-align: center;
  }
  .badge__intro {
    margin: 78px 0 0;
    font-family: "Kaushan Script", cursive;
    font-size: 66px;
    line-height: 1;
  }
  .badge__title {
    margin: 8px 0 0;
    font-family: "Anton", sans-serif;
    font-size: 94px;
    line-height: 1.02;
    letter-spacing: 1px;
  }
  .brand {
    display: flex;
    align-items: center;
    justify-content: center;
    gap: 10px;
    margin-top: 34px;
  }
  .brand__dot {
    width: 16px;
    height: 16px;
    border-radius: 50%;
    background: var(--sun);
  }
  .brand__name {
    font-family: "Montserrat", sans-serif;
    font-weight: 700;
    font-size: 24px;
    letter-spacing: 2px;
    color: var(--deep);
  }
  .details {
    position: absolute;
    top: 800px;
    left: 0;
    width: 928px;
    height: 134px;
  }
  .details__divider {
    position: absolute;
    top: 0;
    width: 2px;
    height: 134px;
    background: rgba(255,255,255,0.85);
  }
  .details__when {
    position: absolute;
    left: 56px;
    top: 12px;
    font-weight: 800;
    font-size: 27px;
    line-height: 1.02;
  }
  .details__when sup { font-size: 15px; }
  .details__when small { font-size: 15px; }
  .script {
    font-family: "Kaushan Script", cursive;
    font-weight: 400;
  }
  .details__where {
    position: absolute;
    left: 258px;
    width: 410px;
    top: -6px;
    text-align: center;
    font-weight: 500;
    font-size: 27px;
    line-height: 1.05;
  }
  .details__where strong { font-weight: 800; }
  .details__with {
    position: absolute;
    right: 56px;
    top: 14px;
    text-align: right;
    font-weight: 800;
    font-size: 27px;
    line-height: 1;
  }
  .gallery {
    position: absolute;
    left: 17px;
    top: 960px;
    width: 894px;
    height: 148px;
    display: flex;
    gap: 2px;
  }
  .gallery__photo { flex: 1; height: 100%; }
  .gallery__photo--pool { background: linear-gradient(180deg, #a9cde4 0%, #7fb6cf 45%, #3c6f70 100%); }
  .gallery__photo--living { background: linear-gradient(180deg, #eef1f2 0%, #d7dcdf 55%, #6d7478 100%); }
  .gallery__photo--bedroom { background: linear-gradient(180deg, #e3efe9 0%, #f1f3f2 55%, #c9c5b9 100%); }
  .gallery__photo--kitchen { background: linear-gradient(180deg, #f4f5f6 0%, #e3e4e6 55%, #d4562f 100%); }
  .gallery__photo--garden { background: linear-gradient(180deg, #8fb3d6 0%, #d9e4ea 50%, #6f8e5a 100%); }
  .notice {
    position: absolute;
    left: 17px;
    top: 1140px;
    width: 894px;
    height: 43px;
    background: var(--band);
    text-align: center;
    font-weight: 700;
    font-size: 22px;
    line-height: 43px;
  }
</style>
</head>
<body>
<main class="poster">
  <svg class="rays" width="928" height="1200" viewBox="0 0 928 1200" aria-hidden="true">
    <polygon points="0,0 140,0 330,1200 0,1200" fill="#ffffff" opacity="0.08"/>
    <polygon points="300,0 420,0 250,1200 120,1200" fill="#ffffff" opacity="0.07"/>
    <polygon points="560,0 700,0 860,1200 720,1200" fill="#ffffff" opacity="0.07"/>
    <polygon points="820,0 928,0 928,900 640,1200 560,1200" fill="#ffffff" opacity="0.06"/>
  </svg>

  <svg class="wreath" viewBox="0 0 740 720" role="img" aria-label="Tropical wreath of palm leaves, pink and yellow flowers, frangipani and red sunglasses">
    <defs>
      <radialGradient id="wreathTone" cx="50%" cy="52%" r="50%">
        <stop offset="62%" stop-color="#2f8a4c"/>
        <stop offset="80%" stop-color="#1f6a3a"/>
        <stop offset="100%" stop-color="#2f8a4c" stop-opacity="0"/>
      </radialGradient>
    </defs>
    <circle cx="370" cy="380" r="350" fill="url(#wreathTone)"/>
    <circle cx="560" cy="110" r="70" fill="#e7a6d2" opacity="0.85"/>
    <circle cx="220" cy="130" r="55" fill="#fece3e" opacity="0.85"/>
    <circle cx="100" cy="560" r="70" fill="#e7a6d2" opacity="0.85"/>
    <circle cx="640" cy="540" r="55" fill="#fece3e" opacity="0.85"/>
  </svg>

  <section class="badge">
    <p class="badge__intro">it's our</p>
    <h1 class="badge__title">GRAND<br>OPENING!</h1>
    <div class="brand">
      <span class="brand__dot"></span>
      <span class="brand__name">CORAL DRIFT INN</span>
    </div>
  </section>

  <section class="details">
    <div class="details__when">16<sup>th</sup> <span class="script"><small>of</small></span><br>FEBRUARY<br>5:00<small>PM</small><br><span class="script" style="font-size:22px">Happy Hour</span></div>
    <span class="details__divider" style="left:258px"></span>
    <div class="details__where"><span class="script" style="font-size:22px">at</span><br><strong>CORAL DRIFT INN</strong><br>4927 MARLOWE LANE<br>HARLOW KEY,<br>FL 32814</div>
    <span class="details__divider" style="left:667px"></span>
    <div class="details__with"><span class="script" style="font-size:24px">with</span><br>LIVE MUSIC<br>SNACKS &amp;<br>BOOZE</div>
  </section>

  <section class="gallery">
    <div class="gallery__photo gallery__photo--pool" role="img" aria-label="Inn exterior with pool and parking"></div>
    <div class="gallery__photo gallery__photo--living" role="img" aria-label="Renovated living room"></div>
    <div class="gallery__photo gallery__photo--bedroom" role="img" aria-label="Bright bedroom"></div>
    <div class="gallery__photo gallery__photo--kitchen" role="img" aria-label="Kitchen with orange bar stools"></div>
    <div class="gallery__photo gallery__photo--garden" role="img" aria-label="Garden patio with palm trees"></div>
  </section>

  <div class="notice">Property has recently been completely renovated!</div>
</main>
</body>
</html>
```